Business Cards and Stationary
Silver Pine
Professional
Tom Feaster, P.G.
Founder
4718 Wexley Lane
Golden, Colorado 80401
tfeaster@silverpinenviroq.com
www.silverpinenviroq.com
Consulting Compliance Training

```html
<!DOCTYPE html>
<html lang="en">
<head>
<meta charset="utf-8">
<title>Silver Pine Stationery</title>
<link href="https://fonts.googleapis.com/css2?family=Arvo:wght@700&family=Open+Sans:wght@400;600&display=swap" rel="stylesheet">
<style>
:root{
  --backdrop:#a9a9a9;
  --paper:#ffffff;
  --brand-red:#7a1414;
  --ink:#2a2a2a;
  --muted:#6b6b6b;
  --window:#ececec;
}
*{margin:0;padding:0;box-sizing:border-box}
html,body{width:1200px;height:840px;overflow:hidden}
body{background:var(--backdrop);position:relative;font-family:"Open Sans",sans-serif;color:var(--ink)}
.sheet{position:absolute;background:var(--paper);box-shadow:0 2px 6px rgba(0,0,0,.25)}
.brand{position:absolute;display:flex;align-items:center;gap:8px}
.brand-dot{border-radius:50%;background:var(--brand-red);flex:none}
.brand-name{font-family:"Arvo",serif;font-weight:700;color:var(--brand-red);text-transform:uppercase;letter-spacing:.5px;white-space:nowrap}
.footer-line{position:absolute;font-size:7.5px;color:var(--muted);white-space:nowrap;text-align:center;left:0;right:0}

/* envelope */
.envelope{left:41px;top:312px;width:559px;height:199px;overflow:hidden}
.envelope-flap{position:absolute;left:0;top:0}
.envelope .brand{left:48px;top:80px}
.envelope .brand-dot{width:22px;height:22px}
.envelope .brand-name{font-size:22px}
.envelope-window{position:absolute;left:295px;top:96px;width:180px;height:78px;background:var(--window);border:1px solid #d4d4d4;border-radius:3px}
.envelope-rule{position:absolute;left:0;right:0;top:180px;height:2px;background:var(--ink)}
.envelope .footer-line{top:185px}
.envelope-base{position:absolute;left:0;right:0;bottom:0;height:3px;background:var(--ink)}

/* business card front */
.card-front{left:101px;top:552px;width:211px;height:125px}
.card-front .brand{left:10px;top:56px;gap:4px}
.card-front .brand-dot{width:9px;height:9px}
.card-front .brand-name{font-size:10px;letter-spacing:.3px}
.card-person{position:absolute;left:112px;top:22px;font-size:6.5px;line-height:1.3}
.card-person .name{font-weight:600;font-size:7px}
.card-address{position:absolute;left:112px;top:48px;font-size:5px;line-height:1.4;color:var(--muted);white-space:nowrap}
.card-contact{position:absolute;left:112px;top:76px;font-size:5px;line-height:1.4;color:var(--muted);white-space:nowrap}

/* business card back */
.card-back{left:326px;top:552px;width:207px;height:125px;background:var(--brand-red)}
.card-back .brand{right:14px;top:62px;gap:5px}
.card-back .brand-dot{width:10px;height:10px;background:var(--paper)}
.card-back .brand-name{font-size:11px;color:var(--paper)}
.card-back-web{position:absolute;right:14px;top:86px;font-size:6px;color:var(--paper)}

/* letterhead */
.letterhead{left:631px;top:67px;width:497px;height:706px}
.letterhead-band{position:absolute;left:0;right:0;top:0;height:6px;background:var(--brand-red)}
.letterhead .brand{left:38px;top:92px;gap:6px}
.letterhead .brand-dot{width:18px;height:18px}
.letterhead .brand-name{font-size:18px}
.letterhead-rule{position:absolute;left:218px;right:0;top:110px;height:1px;background:var(--brand-red)}
.letterhead .footer-line{top:680px}
.letterhead-base{position:absolute;left:0;right:0;bottom:0;height:6px;background:var(--brand-red)}
</style>
</head>
<body>

<section class="sheet envelope">
  <svg class="envelope-flap" width="559" height="80" viewBox="0 0 559 80" aria-hidden="true">
    <path d="M0 0H559V14Q420 18 300 66Q280 74 259 66Q139 18 0 14Z" fill="#7a1414"/>
    <path d="M0 14Q139 18 259 66Q280 74 300 66Q420 18 559 14" fill="none" stroke="#2a2a2a" stroke-width="2"/>
    <circle cx="279.5" cy="18" r="6" fill="#ffffff"/>
  </svg>
  <div class="brand"><span class="brand-dot"></span><span class="brand-name">Silver Pine</span></div>
  <div class="envelope-window"></div>
  <div class="envelope-rule"></div>
  <p class="footer-line">4718 Wexley Lane Golden, Colorado 80401 &nbsp;|&nbsp; P: 303-555-0142 &nbsp;|&nbsp; www.silverpinenviroq.com</p>
  <div class="envelope-base"></div>
</section>

<section class="sheet card-front">
  <div class="brand"><span class="brand-dot"></span><span class="brand-name">Silver Pine</span></div>
  <div class="card-person">
    <p class="name">Tom Feaster, P.G.</p>
    <p>Founder</p>
  </div>
  <div class="card-address">
    <p>4718 Wexley Lane</p>
    <p>Golden, Colorado 80401</p>
  </div>
  <div class="card-contact">
    <p>T: 303.555.0142</p>
    <p>E: tfeaster@silverpinenviroq.com</p>
  </div>
</section>

<section class="sheet card-back">
  <div class="brand"><span class="brand-dot"></span><span class="brand-name">Silver Pine</span></div>
  <p class="card-back-web">www.silverpinenviroq.com</p>
</section>

<section class="sheet letterhead">
  <div class="letterhead-band"></div>
  <div class="brand"><span class="brand-dot"></span><span class="brand-name">Silver Pine</span></div>
  <div class="letterhead-rule"></div>
  <p class="footer-line">4718 Wexley Lane Golden, Colorado 80401 &nbsp;|&nbsp; P: 303-555-0142 &nbsp;|&nbsp; www.silverpinenviroq.com</p>
  <div class="letterhead-base"></div>
</section>

</body>
</html>
```